COMING SOON PAGE for BEAUTY WEBSITE

Looking for a very beautiful, high end coming soon page for the site, www.glowparlorqz.com

looking for the site to have a bit of text and fade thru a few images -- beautiful fonts, modern airy feel.

Text on page:

it doesn't have to be complicated
glowparlorqz.com coming soon
beauty, simplified.

Please use all lowercase and place the logo somewhere on the page...logo attached and images attached -- happy to provide more images if necessary

You can play with images, zoom in, dont need to use whole image, etc....modern, classy, airy.

thanks.

Target Market(s)

35-60 year old women, modern, elegant, look conscious

Number of Pages Required

1 page

Font styles to use
Sans Serif

Requirements
Must have
• Images fade from one to other slowly and elegantly -- or slide, etc..some sort of elegant transition
• Opaque, airy feel
• logo must be present and easy to identify
Should not have
• NO SOUND
• NO SCRIPT TEXT

```html
<!DOCTYPE html>
<html lang="en">
<head>
<meta charset="utf-8">
<title>glowparlorqz — coming soon</title>
<link rel="stylesheet" href="https://fonts.googleapis.com/css2?family=Nunito+Sans:wght@200;300;400&family=Questrial&display=swap">
<style>
  :root {
    --paper: #ffffff;
    --ink: #0a0a0a;
    --ink-soft: #5a5a5a;
    --frame: #1a1a1a;
    --photo-light: #f3f1ef;
    --photo-hair: #9a6a45;
    --photo-skin: #e8cbb6;
  }
  * { margin: 0; padding: 0; box-sizing: border-box; }
  html, body {
    width: 1200px;
    height: 665px;
    overflow: hidden;
    background: var(--paper);
  }
  .page {
    position: relative;
    width: 1200px;
    height: 665px;
    background: var(--paper);
    border-left: 2px solid var(--frame);
    border-right: 2px solid var(--frame);
    color: var(--ink);
    font-family: "Nunito Sans", sans-serif;
    text-align: center;
  }
  .brand-name {
    position: absolute;
    top: 24px;
    left: 0;
    right: 0;
    font-family: "Questrial", sans-serif;
    font-size: 44px;
    font-weight: 400;
    letter-spacing: 0.01em;
    line-height: 1;
    color: var(--ink);
  }
  .hero-photo {
    position: absolute;
    left: 415px;
    top: 94px;
    width: 374px;
    height: 374px;
  }
  .headline {
    position: absolute;
    top: 478px;
    left: 0;
    right: 0;
    font-size: 54px;
    font-weight: 400;
    letter-spacing: 0.2em;
    padding-left: 0.2em;
    line-height: 1;
  }
  .tagline {
    position: absolute;
    top: 553px;
    left: 0;
    right: 0;
    font-size: 16px;
    font-weight: 300;
    color: var(--ink-soft);
    line-height: 1;
  }
  .site-address {
    position: absolute;
    top: 576px;
    left: 0;
    right: 0;
    font-size: 32px;
    font-weight: 300;
    letter-spacing: 0.02em;
    line-height: 1;
  }
  .signoff {
    position: absolute;
    top: 616px;
    left: 0;
    right: 0;
    font-size: 15px;
    font-weight: 300;
    color: var(--ink-soft);
    line-height: 1;
  }
</style>
</head>
<body>
  <main class="page">
    <header class="brand-name">glowparlorqz</header>

    <svg class="hero-photo" viewBox="0 0 374 374" role="img" aria-label="Portrait photo of a woman lying down with closed eyes, long brown dreadlocks fanned out around her head on a white background">
      <defs>
        <radialGradient id="hero-tones" cx="48%" cy="62%" r="60%">
          <stop offset="0%" stop-color="var(--photo-skin)"/>
          <stop offset="35%" stop-color="#c9a184"/>
          <stop offset="60%" stop-color="var(--photo-hair)" stop-opacity="0.55"/>
          <stop offset="100%" stop-color="var(--photo-light)"/>
        </radialGradient>
      </defs>
      <circle cx="187" cy="187" r="187" fill="url(#hero-tones)"/>
    </svg>

    <h1 class="headline">coming soon</h1>
    <p class="tagline">it doesn't have to be complicated</p>
    <p class="site-address">glowparlorqz.com</p>
    <p class="signoff">beauty simplified</p>
  </main>
</body>
</html>
```